Poster Design for a tea beverage brand - seasonal product "Peach Oolong Fizz"

We're chain of bubble tea beverage stores, located mainly in New York, and we're looking for professional poster design for our new seasonal product - Peach Oolong Fizz(Please note there's no boba in this product). Our brand spirit is to deliver the most authentic flavor of tea from Taiwan. We want the style of the poster to be lovely and energetic that targets at customers around 18-35 age group, both male and female. We would like to see an image of spring felling, expressing the freshness and tasty of our products. Attached are some posters, whose styles are similar to what we want. Also attached our current product photo and some similar product photos downloaded from website for your reference.

```html
<!DOCTYPE html>
<html lang="en">
<head>
<meta charset="utf-8">
<title>Peach Oolong Fizz Poster</title>
<link href="https://fonts.googleapis.com/css2?family=Questrial&family=Comfortaa:wght@500&family=Leckerli+One&display=swap" rel="stylesheet">
<style>
  :root {
    --sky: #58ade6;
    --mint: #a9cfc2;
    --butter: #f2c766;
    --tangerine: #f08a3a;
    --crimson: #e8283c;
    --steel: #4a4a4e;
    --steel-light: #8a8a90;
    --leaf: #8dc63f;
    --white: #ffffff;
    --brew-top: #f6c64a;
    --brew-bottom: #e79a1e;
  }
  html, body {
    margin: 0;
    padding: 0;
    overflow: hidden;
    background: #ffffff;
  }
  .poster {
    position: relative;
    width: 900px;
    height: 1200px;
    overflow: hidden;
    background: linear-gradient(180deg,
      var(--sky) 0%,
      #7fbfd8 15%,
      var(--mint) 30%,
      #dccf8a 42%,
      var(--butter) 50%,
      #f3a64a 62%,
      var(--tangerine) 72%,
      #ee5a3c 84%,
      var(--crimson) 100%);
  }
  .headline-word {
    position: absolute;
    margin: 0;
    line-height: 1;
    white-space: nowrap;
  }
  .fruit-name {
    left: 150px;
    top: 108px;
    font-family: "Questrial", sans-serif;
    font-size: 158px;
    letter-spacing: -2px;
    color: var(--steel);
    -webkit-text-stroke: 2px #2a2a2e;
    text-shadow: 0 3px 0 var(--steel-light), 3px 5px 6px rgba(0,0,0,0.35);
  }
  .fruit-echo {
    left: 150px;
    font-family: "Questrial", sans-serif;
    font-size: 158px;
    letter-spacing: -2px;
    color: rgba(60, 60, 66, 0.55);
  }
  .echo-1 { top: 212px; opacity: 0.9; }
  .echo-2 { top: 316px; opacity: 0.55; }
  .echo-3 { top: 420px; opacity: 0.35; }
  .echo-4 { top: 524px; opacity: 0.25; }
  .echo-5 { top: 628px; opacity: 0.12; }
  .tea-type {
    left: 318px;
    top: 218px;
    font-family: "Leckerli One", cursive;
    font-size: 150px;
    color: var(--leaf);
    transform: rotate(-4deg);
    text-shadow:
      4px 0 0 var(--white), -4px 0 0 var(--white),
      0 4px 0 var(--white), 0 -4px 0 var(--white),
      3px 3px 0 var(--white), -3px -3px 0 var(--white),
      3px -3px 0 var(--white), -3px 3px 0 var(--white),
      8px 10px 8px rgba(0,0,0,0.45);
  }
  .drink-style {
    left: 232px;
    top: 396px;
    font-family: "Comfortaa", sans-serif;
    font-weight: 500;
    font-size: 250px;
    letter-spacing: -6px;
    color: var(--white);
    text-shadow: 0 0 14px rgba(230, 255, 140, 0.95), 0 0 30px rgba(220, 255, 120, 0.7);
  }
  .drink-glow {
    position: absolute;
    left: 230px;
    top: 700px;
    width: 440px;
    height: 460px;
    border-radius: 50%;
    background: radial-gradient(ellipse at center, rgba(255,255,255,0.85) 0%, rgba(255,245,210,0.55) 45%, rgba(255,255,255,0) 72%);
  }
  .drink-photo {
    position: absolute;
    left: 278px;
    top: 738px;
    width: 344px;
    height: 390px;
  }
  .brand-name {
    position: absolute;
    left: 330px;
    top: 955px;
    margin: 0;
    font-family: "Questrial", sans-serif;
    font-size: 30px;
    color: #6b4a12;
    transform: rotate(-6deg);
  }
</style>
</head>
<body>
  <main class="poster">
    <p class="headline-word fruit-echo echo-1" aria-hidden="true">PEACH</p>
    <p class="headline-word fruit-echo echo-2" aria-hidden="true">PEACH</p>
    <p class="headline-word fruit-echo echo-3" aria-hidden="true">PEACH</p>
    <p class="headline-word fruit-echo echo-4" aria-hidden="true">PEACH</p>
    <p class="headline-word fruit-echo echo-5" aria-hidden="true">PEACH</p>

    <h1 class="headline-word fruit-name">PEACH</h1>
    <p class="headline-word tea-type">Oolong</p>
    <p class="headline-word drink-style">Fizz</p>

    <div class="drink-glow" aria-hidden="true"></div>
    <svg class="drink-photo" viewBox="0 0 344 390" role="img" aria-label="Photo of an iced Peach Oolong Fizz in a clear branded cup">
      <defs>
        <linearGradient id="brew" x1="0" y1="0" x2="0" y2="1">
          <stop offset="0" stop-color="var(--brew-top)"/>
          <stop offset="1" stop-color="var(--brew-bottom)"/>
        </linearGradient>
      </defs>
      <path d="M6 40 L338 40 L300 384 L46 384 Z" fill="url(#brew)"/>
      <ellipse cx="172" cy="40" rx="166" ry="30" fill="#f3dc9a"/>
    </svg>
    <p class="brand-name">Leafwell</p>
  </main>
</body>
</html>
```